Stationary for Wealth Management Firm

We need stationary design based on our new business cards. We would like it to be simple, clean and understated. A lot of our clients are seniors so the fonts cannot be too small. Our colors are dark blue and light grey.

This is what we need:

1. Letterhead US Letter – 8.5" x 11" CMYK 300 DPI
2. Invoice US Letter – 8.5" x 11" CMYK 300 DPI
3. Fax Cover Sheet US Letter – 8.5" x 11" CMYK 300 DPI
4. Email Signature

Including: logo, motto, address with phone and fax numbers, web address, and compliance disclosure.

5. Standard Envelope #10 – 9,5” x 4,125” CMYK 300 Dpi
6. Large Envelope – 9” x 12” CMYK 300 Dpi

Including: logo, motto, addresses without phone and fax numbers, web address, and compliance disclosure.

7. Letterhead Follower US Letter – 8.5" x 11" CMYK 300 DPI

Including: logo, motto, and web address.

8. Flat Invitation Cards – 6” x 4” CMYK 300 Dpi
9. Pocket Folder – 9" x 12”, CMYK 300 Dpi

Including: logo and motto.

Here is the info:

Company: Copperlake Asset Partners LLC
Address 1: 4817 Harmon Blvd. Suite K-12, Willow Grove, PA, 19090
Phone 1: 1-215-555-0173
Address 2: 618 Larkspur Lane, Fernhollow Twp., PA, 19000
Phone 2: 1-610-555-0149
Fax: 1-484-555-0186
Motto: A Tradition of Trust (in grey #A8A8A8 and US Declaration font)
Web address: www.copperlakeassets.example
Compliance disclosure: Securities and Advisory Services offered through QRV Capital. Member NASTO/CMBF.
Logo: in uploaded files

Industry/Entity Type

Business

Requirements
Must have
• Need to blend the business card look and feel with the brochure/website look and feel.

```html
<!DOCTYPE html>
<html lang="en">
<head>
<meta charset="utf-8">
<title>Email Signature – Copperlake Asset Partners</title>
<link rel="stylesheet" href="https://fonts.googleapis.com/css2?family=Arimo:wght@400;700&display=swap">
<style>
  :root {
    --navy: #262a4c;
    --ink: #2b2b2b;
    --grey: #7a7a7a;
    --rule: #8c8c8c;
    --page: #ffffff;
  }
  * { box-sizing: border-box; margin: 0; padding: 0; }
  html, body {
    width: 1200px;
    height: 1000px;
    overflow: hidden;
    background: var(--page);
    font-family: "Arimo", Arial, sans-serif;
  }
  .canvas {
    width: 1200px;
    height: 1000px;
    display: flex;
    align-items: center;
    justify-content: center;
  }
  .signature { width: 800px; }
  .signer-name {
    font-size: 29px;
    color: var(--navy);
    letter-spacing: 0.5px;
  }
  .signer-title {
    font-size: 22px;
    color: var(--grey);
    margin-top: 6px;
  }
  .double-rule {
    margin-top: 42px;
    height: 6px;
    border-top: 2px solid var(--rule);
    border-bottom: 2px solid var(--rule);
  }
  .signature-body {
    display: flex;
    margin-top: 38px;
  }
  .brand {
    width: 268px;
    display: flex;
    flex-direction: column;
    align-items: center;
    justify-content: flex-end;
    padding-bottom: 6px;
  }
  .brand-square {
    width: 70px;
    height: 70px;
    background: var(--navy);
    margin-bottom: 26px;
  }
  .brand-name {
    font-size: 21px;
    color: var(--navy);
    text-align: center;
    line-height: 1.3;
  }
  .contact { flex: 1; }
  .contact-address,
  .contact-phones {
    font-size: 22px;
    color: var(--ink);
    line-height: 1.35;
  }
  .contact-phones b { color: var(--navy); }
  .disclosure {
    margin-top: 30px;
    font-size: 16px;
    color: var(--grey);
    line-height: 1.35;
  }
  .web {
    margin-top: 38px;
    font-size: 24px;
    color: var(--ink);
  }
  .web b { color: var(--navy); }
</style>
</head>
<body>
<main class="canvas">
  <section class="signature">
    <p class="signer-name">DANIEL WHITFORD</p>
    <p class="signer-title">Managing Director</p>
    <div class="double-rule"></div>
    <div class="signature-body">
      <div class="brand">
        <div class="brand-square"></div>
        <p class="brand-name">COPPERLAKE<br>ASSET PARTNERS</p>
      </div>
      <div class="contact">
        <p class="contact-address">618 Larkspur Lane, Fernhollow Twp., PA, 19000</p>
        <p class="contact-phones"><b>[ T ]</b> 1-610-555-0149, <b>[ F ]</b> 1-484-555-0186</p>
        <p class="disclosure">Securities and Advisory Services offered<br>through QRV Capital. Member NASTO/CMBF</p>
        <p class="web">www.<b>copperlakeassets</b>.example</p>
      </div>
    </div>
  </section>
</main>
</body>
</html>
```